Brightholm painting

Am looking for a lawn sign design for my paintings company.
I also attached my business card a example

Phone number of the business +1(431)572-8846
Key words:Free estimates|pressure washing |Residential| Commercial | Interior | Exterior

```html
<!DOCTYPE html>
<html lang="en">
<head>
<meta charset="utf-8">
<title>Brightholm Painting – Lawn Sign</title>
<link href="https://fonts.googleapis.com/css2?family=Montserrat:wght@400;600;700;800&display=swap" rel="stylesheet">
<style>
  :root {
    --sky: #03a8e0;
    --orange: #f5891f;
    --orange-light: #fbb116;
    --paper: #f4f4f4;
    --ink: #333333;
    --backdrop: #e6e8e4;
    --splash-yellow: #ffd400;
    --splash-green: #55b948;
    --splash-purple: #7b3f9a;
  }
  html, body {
    margin: 0;
    padding: 0;
    width: 1195px;
    height: 1200px;
    overflow: hidden;
    background: var(--backdrop);
  }
  .lawn-sign {
    position: absolute;
    left: 0;
    top: 153px;
    width: 1195px;
    height: 894px;
    background: var(--paper);
    font-family: "Montserrat", sans-serif;
    overflow: hidden;
  }
  .sign-shapes {
    position: absolute;
    inset: 0;
  }
  .brand-name {
    position: absolute;
    left: 452px;
    top: 78px;
    width: 684px;
    margin: 0;
    text-align: center;
    color: var(--sky);
    font-weight: 700;
    font-size: 58px;
    line-height: 1.08;
    letter-spacing: 4px;
    text-transform: uppercase;
  }
  .service-label {
    position: absolute;
    top: 428px;
    width: 240px;
    margin: 0;
    text-align: center;
    color: var(--ink);
    font-weight: 400;
    font-size: 28px;
    line-height: 1.3;
    letter-spacing: 1px;
  }
  .service-label.pressure { left: 436px; }
  .service-label.sectors { left: 688px; top: 432px; }
  .service-label.surfaces { left: 936px; }
  .estimate-call {
    position: absolute;
    left: 450px;
    top: 640px;
    width: 330px;
    margin: 0;
    text-align: center;
    color: #ffffff;
    font-weight: 700;
    text-transform: uppercase;
  }
  .estimate-call .lead {
    display: block;
    font-size: 30px;
    letter-spacing: 2px;
    line-height: 1.05;
  }
  .estimate-call .offer {
    display: block;
    font-size: 44px;
    font-weight: 800;
    letter-spacing: 2px;
    line-height: 0.95;
  }
  .phone-number {
    position: absolute;
    left: 246px;
    top: 790px;
    margin: 0;
    color: #ffffff;
    font-weight: 700;
    font-size: 88px;
    line-height: 1;
    letter-spacing: 1px;
    white-space: nowrap;
  }
</style>
</head>
<body>
<main class="lawn-sign">
  <svg class="sign-shapes" width="1195" height="894" viewBox="0 0 1195 894">
    <defs>
      <linearGradient id="splash-tones" x1="0" y1="0" x2="1" y2="1">
        <stop offset="0" stop-color="var(--splash-yellow)"/>
        <stop offset="0.3" stop-color="var(--sky)"/>
        <stop offset="0.6" stop-color="var(--splash-purple)"/>
        <stop offset="0.85" stop-color="var(--splash-green)"/>
        <stop offset="1" stop-color="var(--splash-yellow)"/>
      </linearGradient>
      <linearGradient id="badge-fill" x1="0" y1="0" x2="1" y2="1">
        <stop offset="0" stop-color="var(--orange)"/>
        <stop offset="1" stop-color="var(--orange-light)"/>
      </linearGradient>
    </defs>

    <path class="paint-splash" role="img" aria-label="Colourful paint splatter of yellow, blue, purple and green"
          d="M0,0 H290 C360,110 450,250 430,420 C420,560 360,640 300,690 L0,600 Z"
          fill="url(#splash-tones)"/>

    <path class="accent-band" d="M0,578 Q610,970 1195,527 L1195,894 L0,894 Z" fill="var(--orange)"/>
    <path class="accent-gap" d="M0,598 Q610,978 1195,552" fill="none" stroke="#ffffff" stroke-width="3"/>

    <circle class="estimate-badge" cx="615" cy="799" r="205" fill="url(#badge-fill)"/>
    <circle class="estimate-badge-ring" cx="615" cy="799" r="196" fill="none" stroke="#ffffff" stroke-width="1.5"/>

    <path class="contact-band" d="M0,612 Q610,985 1195,570 L1195,894 L0,894 Z" fill="var(--sky)"/>

    <g class="service-dividers" stroke="var(--orange)" stroke-width="2">
      <line x1="661" y1="322" x2="661" y2="497"/>
      <line x1="946" y1="322" x2="946" y2="497"/>
    </g>

    <g class="icon-pressure-washer" fill="var(--sky)">
      <rect x="532" y="334" width="32" height="46" rx="8"/>
      <circle cx="548" cy="362" r="7" fill="#ffffff"/>
      <rect x="525" y="378" width="46" height="6" rx="2"/>
      <path d="M548,334 C540,310 560,300 568,312" fill="none" stroke="var(--sky)" stroke-width="3"/>
      <line x1="568" y1="312" x2="588" y2="362" stroke="var(--sky)" stroke-width="5" stroke-linecap="round"/>
      <circle cx="590" cy="372" r="9"/>
    </g>

    <g class="icon-office-building" fill="var(--sky)">
      <rect x="786" y="318" width="43" height="78"/>
      <g fill="#ffffff">
        <rect x="792" y="326" width="6" height="6"/><rect x="804" y="326" width="6" height="6"/><rect x="816" y="326" width="6" height="6"/>
        <rect x="792" y="339" width="6" height="6"/><rect x="804" y="339" width="6" height="6"/><rect x="816" y="339" width="6" height="6"/>
        <rect x="792" y="352" width="6" height="6"/><rect x="804" y="352" width="6" height="6"/><rect x="816" y="352" width="6" height="6"/>
        <rect x="792" y="365" width="6" height="6"/><rect x="804" y="365" width="6" height="6"/><rect x="816" y="365" width="6" height="6"/>
      </g>
    </g>

    <g class="icon-house" fill="none" stroke="var(--sky)" stroke-width="6" stroke-linejoin="round">
      <path d="M1030,354 L1056,328 L1082,354"/>
      <path d="M1036,350 V392 H1076 V350"/>
      <line x1="1074" y1="322" x2="1074" y2="340"/>
      <g fill="var(--sky)" stroke="none">
        <rect x="1046" y="368" width="6" height="24"/>
        <rect x="1060" y="364" width="6" height="28"/>
      </g>
    </g>

    <g class="icon-phone">
      <circle cx="189" cy="834" r="38" fill="#ffffff"/>
      <path d="M176,812 l9,-3 l6,14 l-7,5 c2,8 6,14 13,18 l6,-6 l13,8 l-3,9 c-20,2 -42,-22 -37,-45 z" fill="var(--sky)"/>
    </g>
  </svg>

  <h1 class="brand-name">Brightholm painting</h1>

  <p class="service-label pressure">Pressure<br>Washing</p>
  <p class="service-label sectors">Residential &amp;<br>Commercial</p>
  <p class="service-label surfaces">Interior &amp;<br>Exterior</p>

  <p class="estimate-call">
    <span class="lead">Call us for</span>
    <span class="offer">Free</span>
    <span class="offer">Estimate</span>
  </p>

  <p class="phone-number">+1(431) 572-8846</p>
</main>
</body>
</html>
```